Folded Business Cards for Guarantee, Layaway & The Fine Print

I am looking for a set of (3) folded business for our guarantee, layaway and fine print policies. I would like the same design for each of these cards, with the exception of the picture, title and verbiage.
The front of each card must include our logo, the title of the card (Our Guarantee, Layaway or The Fine Print,) and a picture of a piece of jewelry. The inside of the card should state our policies. The back of the card should have our logo, address (Sandhollow Drive #9, Alderwick, NW 03871,) phone # (603-555-0148) email & web address (info@kastonjewelry.example, www.kastonjewelry.example) and social media icons (FB, Twitter, Pinterest, Instagram)

The layaway card needs a place for the customer's signature.

I was thinking the orientation of the card should be vertical but if the right design ends up being horizontal, I'm ok with that. I do have concerns about readability and that this may be too much information for a folded business card. So, I am open to either changing the front & back, if need be or going to a different format (standard postcard size. Verbiage may also need to be trimmed down, but I need to know what is possible first.

Our branding colors are espresso brown & coppery orange so please do not stray from this color palette. The font of our logo is joefin. I would like the verbiage of the cards to be in quattrocento sans font. We would like a modern & clean look please.

Attached, please find our logo, policies and jewelry pictures. For picture placement, please do the following: Layaway Card (Quartz & onyx pendant,) The Fine Print Card (Orange Garnet Pendant,) Our Guarantee (triple Green Tourmaline Ring.)

```html
<!DOCTYPE html>
<html lang="en">
<head>
<meta charset="utf-8">
<title>Kaston Layaway Card</title>
<link rel="stylesheet" href="https://fonts.googleapis.com/css2?family=Quattrocento+Sans:wght@400;700&display=swap">
<style>
  :root {
    --espresso: #2a1810;
    --copper: #d2702a;
    --paper: #ffffff;
    --ink: #2b2420;
    --backdrop: #e9e8ec;
    --body-font: "Quattrocento Sans", sans-serif;
  }
  * { box-sizing: border-box; margin: 0; padding: 0; }
  html, body { width: 1200px; height: 900px; overflow: hidden; }
  body {
    background: var(--backdrop);
    position: relative;
    font-family: var(--body-font);
  }
  .spread {
    position: absolute;
    top: 190px;
    display: flex;
    height: 520px;
    box-shadow: 0 10px 30px rgba(0,0,0,0.15);
  }
  .spread--outside { left: 150px; }
  .spread--inside { left: 640px; }
  .panel { width: 205px; height: 100%; position: relative; }
  .panel + .panel { border-left: 1px solid rgba(0,0,0,0.08); }

  .brand-name {
    font-family: var(--body-font);
    font-weight: 400;
    line-height: 1;
  }

  /* Back panel */
  .panel--back {
    background: var(--espresso);
    color: var(--copper);
    padding: 0 18px 40px;
    display: flex;
    flex-direction: column;
    justify-content: flex-end;
  }
  .panel--back .brand-name { font-size: 46px; }
  .contact {
    font-size: 13px;
    line-height: 1.4;
    margin-top: 18px;
    text-align: right;
    font-style: normal;
  }
  .social {
    display: flex;
    gap: 12px;
    margin-top: 16px;
    list-style: none;
  }
  .social li {
    width: 22px; height: 22px;
    border-radius: 50%;
    background: var(--copper);
  }

  /* Front panel */
  .panel--front { background: var(--paper); display: flex; flex-direction: column; }
  .title-band {
    background: var(--espresso);
    height: 52px;
    display: flex;
    align-items: center;
    justify-content: center;
  }
  .card-title {
    font-variant: small-caps;
    font-weight: 400;
    font-size: 19px;
    color: var(--copper);
    letter-spacing: 1px;
  }
  .jewelry-photo { display: block; margin: 6px auto 0; }
  .panel--front .brand-block {
    color: var(--espresso);
    padding: 0 20px;
    margin-top: auto;
    margin-bottom: 44px;
    text-align: right;
  }
  .panel--front .brand-name { font-size: 46px; }

  /* Inside panels */
  .panel--inside {
    background: var(--paper);
    color: var(--ink);
    padding: 24px 16px;
    font-size: 13.5px;
    line-height: 1.3;
  }
  .panel--inside h2 {
    font-size: 12.5px;
    font-weight: 700;
    margin-bottom: 20px;
    white-space: nowrap;
  }
  .panel--inside p { text-align: justify; margin-bottom: 16px; }
</style>
</head>
<body>
  <section class="spread spread--outside">
    <div class="panel panel--back">
      <div class="brand-name">Kaston</div>
      <address class="contact">
        Sandhollow Drive #9,<br>
        Birchway Plaza<br>
        Alderwick, NW 03871<br>
        (603) 555-0148<br>
        info@kastonjewelry.example<br>
        www.kastonjewelry.example
      </address>
      <ul class="social" aria-label="Social media">
        <li></li><li></li><li></li><li></li>
      </ul>
    </div>
    <div class="panel panel--front">
      <div class="title-band"><h1 class="card-title">Layaway</h1></div>
      <svg class="jewelry-photo" width="160" height="290" viewBox="0 0 160 290" role="img" aria-label="Photo of quartz and onyx pendant on a gold chain">
        <defs>
          <linearGradient id="pendant-tone" x1="0" y1="0" x2="0" y2="1">
            <stop offset="0" stop-color="#f4f1ee"/>
            <stop offset="0.35" stop-color="#b89a86"/>
            <stop offset="0.55" stop-color="#3a2a24"/>
            <stop offset="1" stop-color="#f7f6f5"/>
          </linearGradient>
        </defs>
        <rect x="0" y="0" width="160" height="290" fill="url(#pendant-tone)"/>
      </svg>
      <div class="brand-block">
        <div class="brand-name">Kaston</div>
      </div>
    </div>
  </section>

  <section class="spread spread--inside">
    <div class="panel panel--inside">
      <h2>Something to Look Forward to…</h2>
      <p>Special occasion shopping made easy.</p>
      <p>Take home the jewelry you love after 6 monthly payments or 3 monthly payments for sale merchandize.</p>
      <p>A 20% deposit secures your layaway, interest-free.</p>
      <p>No approval process.</p>
      <p>No finance charges or hidden fees.</p>
      <p>A 5% restocking fee will be charged for layaways cancelled after 30 days.</p>
    </div>
    <div class="panel panel--inside">
      <p>If your layaway is cancelled after 30 days, either by you or us, all deposits &amp; payments will be converted to store credit. Restocking fee applies.</p>
      <p>Custom jewelry &amp; special orders placed on layaway require a 50% deposit and are non-cancellable &amp; non-refundable.</p>
      <p>Kaston's retains the right to cancel any layaway, at any time, for late or inconsistent payments. Cancellation fees &amp; policies, as stated above, will apply.</p>
    </div>
  </section>
</body>
</html>
```